Business card Zottelgarten

Business card is for a self-employed dog trainer with own dog school. Name and logo of the dog school are available. Color specifications as well. The design should be classy and minimalist, but also modern. An already existing idea would be: Front: Only the logo Back: Contact data

Font styles to use
Serif
Sans Serif
Other font styles liked:
• Trajan Pro

Colors
f78f20

Requirements
Must have
• Name: Margit Wendler-Rasch Title: Dipl. Dog Trainer Contain my logo Follow my font and color preferences (see files)

```html
<!DOCTYPE html>
<html lang="de">
<head>
<meta charset="utf-8">
<title>Zottelgarten – Visitenkarte</title>
<link rel="stylesheet" href="https://fonts.googleapis.com/css2?family=Cinzel:wght@400;500&display=swap">
<style>
  :root {
    --brand-orange: #f78f20;
    --card-white: #ffffff;
    --ink: #1c1c1c;
    --backdrop: #ecedef;
    --shadow: rgba(0, 0, 0, 0.28);
  }
  * { box-sizing: border-box; margin: 0; padding: 0; }
  html, body {
    width: 1200px;
    height: 1200px;
    overflow: hidden;
  }
  body {
    position: relative;
    background: var(--backdrop);
    font-family: "Cinzel", serif;
  }
  .card {
    position: absolute;
    width: 770px;
    height: 470px;
    box-shadow: 6px 10px 18px var(--shadow);
  }

  /* Front */
  .card--front {
    left: 140px;
    top: 90px;
    background: var(--brand-orange);
    color: var(--card-white);
  }
  .brand-mark {
    position: absolute;
    left: 50%;
    top: 64px;
    width: 200px;
    height: 200px;
    margin-left: -100px;
    border-radius: 50%;
    background: var(--card-white);
  }
  .brand-name {
    position: absolute;
    left: 0;
    right: 0;
    top: 300px;
    text-align: center;
    font-size: 72px;
    font-weight: 400;
    letter-spacing: 2px;
    line-height: 1;
  }
  .brand-url {
    position: absolute;
    left: 0;
    right: 0;
    top: 392px;
    text-align: center;
    font-size: 22px;
    letter-spacing: 9px;
    line-height: 1;
  }

  /* Back */
  .card--back {
    left: 310px;
    top: 630px;
    background: var(--card-white);
    color: var(--ink);
  }
  .holder {
    position: absolute;
    left: 52px;
    top: 62px;
  }
  .holder__name {
    font-size: 40px;
    font-weight: 400;
    letter-spacing: 1.5px;
    line-height: 1.1;
  }
  .holder__title {
    margin-top: 8px;
    font-size: 27px;
    letter-spacing: 1px;
  }
  .divider {
    position: absolute;
    left: 0;
    right: 0;
    top: 174px;
    height: 14px;
    border-top: 2px solid var(--brand-orange);
    border-bottom: 2px solid var(--brand-orange);
  }
  .contact-list {
    position: absolute;
    left: 52px;
    top: 214px;
    list-style: none;
    font-size: 26px;
    letter-spacing: 1.2px;
  }
  .contact-list li { line-height: 51px; }
</style>
</head>
<body>
  <section class="card card--front" aria-label="Vorderseite">
    <div class="brand-mark" aria-hidden="true"></div>
    <h1 class="brand-name">ZOTTELGARTEN</h1>
    <p class="brand-url">WWW.ZOTTELGARTEN.CH</p>
  </section>

  <section class="card card--back" aria-label="Rückseite">
    <div class="holder">
      <h2 class="holder__name">Margit Wendler-Rasch</h2>
      <p class="holder__title">Dipl. Hundetrainerin</p>
    </div>
    <div class="divider"></div>
    <ul class="contact-list">
      <li>Adresse</li>
      <li>Stadt</li>
      <li>Telefonnummer</li>
      <li>Email</li>
      <li>Webseite</li>
    </ul>
  </section>
</body>
</html>
```